Estate agent needs for sale board design to match their modern approach to selling home.

Need a for sale design for our estate agency business. We are looking for a clean look with a white background but some clever graphical elements to it. I enclose our logo so you can use this.
We need the words 'FOR SALE' and our telephone number prominent. 0808 472 9580 . The size of the boards are 640h x 813w.
Industry/Entity Type
Business
Requirements
Must have
- Colours matching our logo.

```html
<!DOCTYPE html>
<html lang="en">
<head>
<meta charset="utf-8">
<title>For Sale Board – Keyline Homes</title>
<link rel="stylesheet" href="https://fonts.googleapis.com/css2?family=Bebas+Neue&family=Montserrat:wght@600&display=swap">
<style>
  :root {
    --backdrop: #e9ebee;
    --board: #ffffff;
    --brand-pink: #e6358f;
    --brand-green: #8dc63f;
    --brand-grey: #4a4a4a;
    --roof-peach: #fbd9b9;
    --shadow: rgba(0, 0, 0, 0.12);
  }
  html, body {
    margin: 0;
    padding: 0;
    width: 1200px;
    height: 802px;
    overflow: hidden;
    background: var(--backdrop);
  }
  .canvas {
    position: relative;
    width: 1200px;
    height: 802px;
  }
  .sale-board {
    position: absolute;
    left: 142px;
    top: 41px;
    width: 915px;
    height: 720px;
    background: var(--board);
    box-shadow: 0 6px 24px var(--shadow);
    overflow: hidden;
  }
  .roofline-graphic {
    position: absolute;
    left: 73px;
    top: 95px;
    width: 750px;
    height: 200px;
    background: linear-gradient(180deg, var(--brand-pink) 0%, #f08ab8 45%, var(--roof-peach) 100%);
  }
  .headline {
    position: absolute;
    left: 0;
    right: 0;
    top: 282px;
    margin: 0;
    text-align: center;
    font-family: "Bebas Neue", sans-serif;
    font-weight: 400;
    font-size: 270px;
    line-height: 1;
    letter-spacing: 4px;
    color: var(--brand-pink);
  }
  .divider {
    position: absolute;
    left: 0;
    right: 0;
    top: 518px;
    height: 10px;
    background: var(--brand-green);
  }
  .contact-row {
    position: absolute;
    left: 30px;
    right: 30px;
    top: 560px;
    height: 120px;
    display: flex;
    align-items: center;
    justify-content: space-between;
  }
  .agency-name {
    display: flex;
    align-items: center;
    gap: 14px;
    font-family: "Montserrat", sans-serif;
    font-weight: 600;
    font-size: 30px;
    line-height: 1.05;
    color: var(--brand-grey);
    text-transform: uppercase;
  }
  .agency-mark {
    width: 52px;
    height: 52px;
    background: var(--brand-pink);
    flex: none;
  }
  .phone-number {
    font-family: "Bebas Neue", sans-serif;
    font-size: 112px;
    line-height: 1;
    letter-spacing: 2px;
    color: var(--brand-pink);
  }
</style>
</head>
<body>
  <main class="canvas">
    <section class="sale-board">
      <div class="roofline-graphic" role="img" aria-label="Pink and peach illustrated rooftops with chimneys and small blue windows"></div>
      <h1 class="headline">FOR SALE</h1>
      <div class="divider"></div>
      <div class="contact-row">
        <div class="agency-name">
          <span class="agency-mark"></span>
          <span>Keyline<br>Homes</span>
        </div>
        <div class="phone-number">0808 472 9580</div>
      </div>
    </section>
  </main>
</body>
</html>
```